Kiosk Coin Venture: Safe and Secure Cash Money

Front of card: LOGO

Back of card:
$$$ FREE ATM PLACEMENT $$$
BENIFITS OF HAVING AN ATM AT YOUR BUSINESS
FREE ATM and BTM (Bitcoin) installation, maintenance, and loading.
Lower card processing fees
Stimulate more traffic.
Ease of access for customers
Maintain customers inside location.
Higher tips and spending

Contact me for more information!
Name: Tobias Merlano
Phone: (512) 638-9071 - Call or Text
Email: Tobias@KioskCoin.example

Contact Information for Business Card

The card should be shape of the logo. Only the back will have all the contact and business details.

Requirements
Must have
• The logo itself will be one side, the card will be the shape of the logo. contact details on back side.

```html
<!DOCTYPE html>
<html lang="en">
<head>
<meta charset="utf-8">
<title>Kiosk Coin Venture – Business Card</title>
<link href="https://fonts.googleapis.com/css2?family=Oswald:wght@400&display=swap" rel="stylesheet">
<style>
  :root {
    --backdrop: #858585;
    --card: #222222;
    --card-edge: #161616;
    --gold: #e3b23c;
    --white: #ffffff;
    --silver: #d6d6d6;
  }
  html, body {
    margin: 0;
    padding: 0;
    width: 1075px;
    height: 1200px;
    overflow: hidden;
    background: var(--backdrop);
    font-family: "Oswald", "Arial Narrow", sans-serif;
  }
  p, ul { margin: 0; padding: 0; }
  .canvas {
    position: relative;
    width: 1075px;
    height: 1200px;
  }
  .card {
    position: absolute;
    top: 271px;
    width: 400px;
    height: 659px;
    filter: drop-shadow(2px 4px 4px rgba(0,0,0,0.35));
  }
  .card--back { left: 121px; }
  .card--front { left: 582px; }
  .card__shape {
    position: absolute;
    inset: 0;
  }
  .card__content {
    position: absolute;
    inset: 0;
    text-align: center;
    color: var(--white);
    font-weight: 400;
  }
  .headline {
    position: absolute;
    top: 118px;
    left: 0;
    right: 0;
    color: var(--gold);
    font-size: 28px;
    letter-spacing: -0.8px;
    line-height: 30px;
  }
  .subhead {
    position: absolute;
    top: 181px;
    left: 21px;
    right: 24px;
    padding: 7px 0;
    border-top: 1px solid var(--gold);
    border-bottom: 1px solid var(--gold);
    font-size: 21px;
    line-height: 26px;
    letter-spacing: -0.6px;
    white-space: nowrap;
  }
  .benefits {
    position: absolute;
    top: 236px;
    left: 0;
    right: 0;
    list-style: none;
    font-size: 21px;
    line-height: 26.3px;
    letter-spacing: -0.6px;
  }
  .cta {
    position: absolute;
    top: 460px;
    left: 0;
    right: 0;
    color: var(--gold);
    font-size: 21px;
    letter-spacing: -0.5px;
    line-height: 24px;
  }
  .contact-name {
    position: absolute;
    top: 494px;
    left: 0;
    right: 0;
    font-size: 22px;
    letter-spacing: -0.4px;
    line-height: 26px;
  }
  .contact-rule {
    position: absolute;
    top: 526px;
    left: 171px;
    width: 58px;
    height: 1px;
    background: var(--gold);
  }
  .contact-details {
    position: absolute;
    top: 532px;
    left: 0;
    right: 0;
    font-size: 18px;
    line-height: 24px;
    letter-spacing: -0.5px;
  }
  .brand {
    position: absolute;
    top: 150px;
    left: 0;
    right: 0;
    display: flex;
    flex-direction: column;
    align-items: center;
  }
  .brand__dot {
    width: 60px;
    height: 60px;
    border-radius: 50%;
    background: var(--gold);
    margin-bottom: 30px;
  }
  .brand__name {
    color: var(--silver);
    font-size: 62px;
    font-weight: 400;
    line-height: 1.05;
    text-transform: uppercase;
    letter-spacing: 2px;
    text-align: center;
  }
</style>
</head>
<body>
<div class="canvas">

  <section class="card card--back" aria-label="Card back with services and contact details">
    <svg class="card__shape" width="400" height="659" viewBox="0 0 400 659">
      <path d="M200 0 L400 71 L400 430 C400 535 320 600 200 659 C80 600 0 535 0 430 L0 71 Z" fill="var(--card)" stroke="var(--card-edge)" stroke-width="2"/>
    </svg>
    <div class="card__content">
      <p class="headline">$$$ FREE ATM PLACEMENT $$$</p>
      <p class="subhead">Benifits of having an ATM at your business</p>
      <ul class="benefits">
        <li>FREE ATM and BTM (Bitcoin) installation</li>
        <li>maintenance, and loading.</li>
        <li>Lower card processing fees</li>
        <li>Stimulate more traffic.</li>
        <li>Ease of access for customers</li>
        <li>Maintain customers inside location.</li>
        <li>Higher tips and spending</li>
      </ul>
      <p class="cta">Contact me for more information!</p>
      <p class="contact-name">Tobias Merlano</p>
      <div class="contact-rule"></div>
      <p class="contact-details">(512) 638-9071 - Call or Text<br>Tobias@KioskCoin.example</p>
    </div>
  </section>

  <section class="card card--front" aria-label="Card front with company name">
    <svg class="card__shape" width="400" height="659" viewBox="0 0 400 659">
      <path d="M200 0 L400 71 L400 430 C400 535 320 600 200 659 C80 600 0 535 0 430 L0 71 Z" fill="var(--card)" stroke="var(--card-edge)" stroke-width="2"/>
    </svg>
    <div class="brand">
      <div class="brand__dot"></div>
      <p class="brand__name">Kiosk<br>Coin<br>Venture</p>
    </div>
  </section>

</div>
</body>
</html>
```